Corporate Identity,Logo,Clothing,Letterhead,Business Cards,Signage etc

Name of Business - Hollowell & Brandt Crash Repairs
Colours - Royal Blue, White & Yellow

```html
<!DOCTYPE html>
<html lang="en">
<head>
<meta charset="utf-8">
<title>Hollowell &amp; Brandt Crash Repairs – Stationery</title>
<link rel="stylesheet" href="https://fonts.googleapis.com/css2?family=Open+Sans:wght@400;600&family=Arimo:wght@400;700&family=Cormorant+Garamond:ital,wght@1,500&display=swap">
<style>
  :root{
    --navy:#2b2761;
    --royal:#5e5aa9;
    --lavender:#a9a7da;
    --charcoal:#47444f;
    --white:#ffffff;
    --ink:#333333;
    --stage:#e9e8ee;
  }
  *{margin:0;padding:0;box-sizing:border-box}
  html,body{width:1200px;height:960px;overflow:hidden;background:var(--stage)}
  .canvas{position:relative;width:1200px;height:960px}
  .piece{position:absolute;overflow:hidden;background:var(--white);box-shadow:0 4px 14px rgba(0,0,0,.18)}
  .piece > svg{position:absolute;inset:0}
  .brand-mark{position:absolute;display:flex;align-items:center;justify-content:center;text-align:center;border:2px solid var(--white);border-radius:50%;color:var(--white);font-family:"Open Sans",sans-serif;font-weight:600;line-height:1.15}

  /* Letterhead */
  .letterhead{left:20px;top:18px;width:598px;height:845px}
  .letterhead .brand-mark{left:52px;top:54px;width:114px;height:114px;font-size:13px}
  .salutation{position:absolute;left:135px;top:236px;font:700 11px "Arimo",sans-serif;color:var(--ink)}
  .letter-body{position:absolute;left:135px;top:286px;width:432px;font:400 7.4px/15px "Arimo",sans-serif;color:var(--ink);text-align:justify}
  .letter-body p+p{margin-top:12px}
  .sign-off{position:absolute;left:444px;top:632px;font:400 7.5px "Arimo",sans-serif;color:#777}
  .signature{position:absolute;left:432px;top:646px;width:130px;height:56px;border-radius:6px;background:linear-gradient(135deg,#f3f2f6,#e4e2ec)}
  .signatory{position:absolute;left:444px;top:712px;font:400 8.5px "Arimo",sans-serif;color:#666}
  .signatory small{display:block;font-size:6.5px;margin-top:3px}

  .contact-row{position:absolute;display:flex;align-items:center;font:400 7px "Open Sans",sans-serif;color:var(--navy)}
  .contact-row span{display:flex;align-items:center;gap:5px}
  .icon{width:9px;height:9px;flex:none}
  .letterhead .contact-row{left:216px;top:810px;width:340px;justify-content:space-between}

  /* Business card front */
  .card-front{left:640px;top:90px;width:265px;height:150px}
  .card-front .brand-mark{right:12px;top:12px;width:40px;height:40px;font-size:5px;border-width:1.5px}
  .vehicle-area{position:absolute;left:118px;top:48px;width:110px;height:40px;border-radius:14px 30px 6px 6px;background:linear-gradient(90deg,#e4e0ee,#d8d3e6)}
  .card-name{position:absolute;left:64px;top:62px;font:400 11px "Open Sans",sans-serif;color:var(--navy)}
  .card-front .contact-list{position:absolute;left:64px;top:84px;display:flex;flex-direction:column;gap:6px;font:400 7px "Open Sans",sans-serif;color:var(--navy)}
  .card-front .contact-list span{display:flex;align-items:center;gap:5px}

  /* Business card back */
  .card-back{left:918px;top:90px;width:265px;height:150px;background:var(--royal)}
  .card-back .brand-mark{left:112px;top:22px;width:44px;height:44px;font-size:5.5px;border-width:1.5px}
  .card-back-name{position:absolute;left:0;right:0;top:84px;text-align:center;font:400 12px "Open Sans",sans-serif;color:var(--white)}

  /* Compliments slip */
  .comp-slip{left:630px;top:507px;width:555px;height:262px}
  .comp-slip .brand-mark{left:496px;top:20px;width:50px;height:50px;font-size:6px;border-width:1.5px}
  .comp-title{position:absolute;left:84px;top:28px;font:italic 500 16px "Cormorant Garamond",serif;color:var(--navy)}
  .comp-slip .contact-row{left:38px;top:244px;width:440px;justify-content:space-between;font-size:6.5px}
</style>
</head>
<body>
<div class="canvas">

  <section class="piece letterhead">
    <svg width="598" height="845" viewBox="0 0 598 845">
      <rect width="598" height="845" fill="var(--navy)"/>
      <ellipse cx="690" cy="540" rx="700" ry="660" fill="var(--royal)"/>
      <ellipse cx="672" cy="528" rx="660" ry="625" fill="var(--navy)"/>
      <ellipse cx="664" cy="522" rx="645" ry="612" fill="var(--charcoal)"/>
      <ellipse cx="660" cy="520" rx="630" ry="600" fill="var(--white)"/>
      <line x1="0" y1="150" x2="130" y2="0" stroke="var(--white)" stroke-width="3"/>
    </svg>
    <div class="brand-mark">Hollowell<br>&amp; Brandt</div>
    <p class="salutation">Dear Sir/Madam,</p>
    <div class="letter-body">
      <p>Lorem ipsum dolor sit amet, consectetur adipiscing elit. Vestibulum adipiscing felis ac tortor consectetur feugiat. Etiam malesuada sodales eros ut ornare. Sed lorem eros, mattis id pretium ut, faucibus sit amet quam. Nullam consectetur ultricies ipsum, fringilla porttitor erat ornare at. Sed sit amet dui vel sapien ultrices vulputate. In hac habitasse platea dictumst. Nam est nisi, rhoncus at sagittis a, porttitor adipiscing nulla. Vivamus placerat felis ultrices quam iaculis eget dignissim felis egestas. Integer nec molestie lorem. Sed odio tellus, vulputate sed laoreet non, vulputate id justo. Etiam suscipit, odio vel auctor dictum, felis turpis ullamcorper neque, quis sodales risus metus in magna. Morbi pellentesque justo et quam laoreet facilisis. Aenean placerat, urna ornare aliquet tincidunt, lorem justo molestie ligula, id placerat est metus nec lectus. Nullam eu ipsum quis turpis tristique iaculis rutrum nec nibh. Phasellus risus eros, semper sit amet faucibus sit amet, laoreet et neque. Donec eros sem, viverra dictum faucibus quis, ullamcorper tincidunt nulla.</p>
      <p>Aenean ut congue tellus. Class aptent taciti sociosqu ad litora torquent per conubia nostra, per inceptos himenaeos. Sed facilisis, velit tincidunt pharetra fermentum, urna tortor iaculis erat, vitae sollicitudin leo mauris quis mi. Cras malesuada sem ac ipsum sagittis ultrices. Mauris fermentum porttitor nisi, eu facilisis lorem consectetur et. Suspendisse est elit, scelerisque ac euismod id, scelerisque viverra odio. Nullam scelerisque metus in eros semper congue. Fusce a fermentum est. Ut ac leo dolor. Quisque dignissim mauris a neque luctus pretium ultrices risus sagittis. Aenean quam massa, rutrum ac hendrerit eu, interdum eu nulla. Curabitur a velit mauris, sed porta eros. Cras id egestas sapien. Proin non metus eget felis eleifend adipiscing. Nunc malesuada pharetra blandit.</p>
    </div>
    <p class="sign-off">Your sincerely:</p>
    <div class="signature" role="img" aria-label="Handwritten signature"></div>
    <p class="signatory">Lorem Ipsum<small>Office Maneger</small></p>
    <div class="contact-row">
      <span><svg class="icon" viewBox="0 0 10 10"><circle cx="5" cy="5" r="5" fill="var(--navy)"/><circle cx="5" cy="4.3" r="1.6" fill="var(--white)"/></svg>1 Lorem Ipsum RD DC-123456</span>
      <span><svg class="icon" viewBox="0 0 10 10"><circle cx="5" cy="5" r="5" fill="var(--navy)"/><rect x="3.5" y="2.5" width="3" height="5" rx=".6" fill="var(--white)"/></svg>1234567890</span>
      <span><svg class="icon" viewBox="0 0 10 10"><circle cx="5" cy="5" r="5" fill="var(--navy)"/><rect x="2.5" y="3.5" width="5" height="3" fill="var(--white)"/></svg>www.hollowellbrandt-repairs.com</span>
    </div>
  </section>

  <section class="piece card-front">
    <svg width="265" height="150" viewBox="0 0 265 150">
      <rect width="265" height="150" fill="var(--white)"/>
      <path d="M0 0 H60 Q20 75 60 150 H0 Z" fill="var(--navy)"/>
      <path d="M0 0 H50 Q14 75 50 150 H0 Z" fill="var(--royal)"/>
      <path d="M200 0 H265 V150 Q250 40 200 0 Z" fill="var(--royal)"/>
    </svg>
    <div class="vehicle-area" role="img" aria-label="Faint car silhouette"></div>
    <div class="brand-mark">Hollowell<br>&amp; Brandt</div>
    <p class="card-name">Hollowell &amp; Brandt Crash Repairs</p>
    <div class="contact-list">
      <span><svg class="icon" viewBox="0 0 10 10"><circle cx="5" cy="5" r="5" fill="var(--navy)"/><circle cx="5" cy="4.3" r="1.6" fill="var(--white)"/></svg>1 Lorem Ipsum RD DC-123456</span>
      <span><svg class="icon" viewBox="0 0 10 10"><circle cx="5" cy="5" r="5" fill="var(--navy)"/><rect x="3.5" y="2.5" width="3" height="5" rx=".6" fill="var(--white)"/></svg>1234567890</span>
      <span><svg class="icon" viewBox="0 0 10 10"><circle cx="5" cy="5" r="5" fill="var(--navy)"/><rect x="2.5" y="3.5" width="5" height="3" fill="var(--white)"/></svg>www.hollowellbrandt-repairs.com</span>
    </div>
  </section>

  <section class="piece card-back">
    <svg width="265" height="150" viewBox="0 0 265 150">
      <rect width="265" height="150" fill="var(--royal)"/>
      <path d="M0 0 H30 Q8 75 30 150 H0 Z" fill="var(--navy)"/>
    </svg>
    <div class="brand-mark">Hollowell<br>&amp; Brandt</div>
    <p class="card-back-name">Hollowell &amp; Brandt Crash Repairs</p>
  </section>

  <section class="piece comp-slip">
    <svg width="555" height="262" viewBox="0 0 555 262">
      <rect width="555" height="262" fill="var(--white)"/>
      <path d="M0 0 H100 Q10 60 28 262 H0 Z" fill="var(--navy)"/>
      <path d="M0 0 H78 Q0 60 20 262 H0 Z" fill="var(--lavender)"/>
      <path d="M0 0 H55 Q-5 60 12 262 H0 Z" fill="var(--royal)"/>
      <path d="M0 0 H35 Q-8 60 5 262 H0 Z" fill="var(--navy)"/>
      <rect x="490" y="0" width="65" height="262" fill="var(--navy)"/>
    </svg>
    <div class="brand-mark">Hollowell<br>&amp; Brandt</div>
    <p class="comp-title">with compliments...</p>
    <div class="contact-row">
      <span><svg class="icon" viewBox="0 0 10 10"><circle cx="5" cy="5" r="5" fill="var(--navy)"/><circle cx="5" cy="4.3" r="1.6" fill="var(--white)"/></svg>1 Lorem Ipsum RD DC-123456</span>
      <span><svg class="icon" viewBox="0 0 10 10"><circle cx="5" cy="5" r="5" fill="var(--navy)"/><rect x="3.5" y="2.5" width="3" height="5" rx=".6" fill="var(--white)"/></svg>1234567890</span>
      <span><svg class="icon" viewBox="0 0 10 10"><circle cx="5" cy="5" r="5" fill="var(--navy)"/><rect x="2.5" y="3.5" width="5" height="3" fill="var(--white)"/></svg>www.hollowellbrandt-repairs.com</span>
    </div>
  </section>

</div>
</body>
</html>
```